Marta Business Card

My wife is going to start her own business with renting holiday appartments to tourists. She needs a design for a new business card... and a new web site.
Look at Stayvolt "Erholung auf dem Lindenwäldchen"

Target Market(s)

Give business card to prospects at any situation

Contact Information for Business Card

not sure what this means

Font styles to use
Script

Colors
fec41a
fee18a

Requirements
Must have
• My wife's handwriting is difficult to read:
Entspannen - Loslassen - Auftanken
Marta & das Lindenwäldchen
Urlaub an einem besonderen Ort
Marta Brecke
Grauer Pfad 7
18471 Alt Feldow
post@marta-brecke.de
www.lindenwaeldchen.net
Nice to have
• Beige background
Font like handwriting

```html
<!DOCTYPE html>
<html lang="de">
<head>
<meta charset="utf-8">
<title>Marta &amp; das Lindenwäldchen – Visitenkarte</title>
<link href="https://fonts.googleapis.com/css2?family=Sacramento&family=Dancing+Script:wght@600&family=Didact+Gothic&display=swap" rel="stylesheet">
<style>
  :root {
    --stage: #e4e3e4;
    --paper: #e3d9cf;
    --wave-1: #ddccbc;
    --wave-2: #d9c2ad;
    --wave-3: #d4b89e;
    --wave-4: #cdab8a;
    --wave-line: #c9b6a3;
    --gold: #8a6428;
    --ink: #3b3532;
    --ink-soft: #4a4340;
  }
  * { box-sizing: border-box; margin: 0; padding: 0; }
  html, body { width: 1200px; height: 1200px; overflow: hidden; }
  body {
    background: var(--stage);
    display: flex;
    flex-direction: column;
    align-items: center;
    justify-content: center;
    gap: 60px;
  }
  .card {
    position: relative;
    width: 800px;
    height: 500px;
    background: var(--paper);
    box-shadow: 0 10px 28px rgba(60, 50, 40, 0.18);
    overflow: hidden;
  }
  .card__waves {
    position: absolute;
    inset: 0;
    width: 100%;
    height: 100%;
  }
  .brand {
    position: absolute;
    left: 0;
    right: 0;
    top: 185px;
    text-align: center;
  }
  .brand__name {
    display: block;
    font-family: "Sacramento", cursive;
    font-size: 58px;
    line-height: 1.1;
    white-space: nowrap;
    color: var(--gold);
  }
  .brand__claim {
    display: block;
    margin-top: 2px;
    font-family: "Didact Gothic", sans-serif;
    font-size: 20px;
    letter-spacing: 0.08em;
    text-transform: uppercase;
    white-space: nowrap;
    color: var(--ink);
  }
  .card--back .brand { top: 135px; }
  .tagline {
    position: absolute;
    left: 0;
    right: 0;
    top: 58px;
    text-align: center;
    font-family: "Dancing Script", cursive;
    font-weight: 600;
    font-size: 38px;
    line-height: 1.2;
    white-space: nowrap;
    color: var(--ink);
  }
  .contact {
    position: absolute;
    font-family: "Didact Gothic", sans-serif;
    font-style: normal;
    font-size: 20px;
    letter-spacing: 0.06em;
    line-height: 1.75;
    text-transform: uppercase;
    white-space: nowrap;
    color: var(--ink-soft);
  }
  .contact--online { right: 40px; top: 265px; text-align: right; }
  .contact--address { left: 60px; top: 370px; }
</style>
</head>
<body>

  <section class="card card--front" aria-label="Visitenkarte Vorderseite">
    <svg class="card__waves" viewBox="0 0 800 500" preserveAspectRatio="none" aria-hidden="true">
      <path d="M560 0 C520 110 560 170 500 260 C450 340 440 420 400 500 L800 500 L800 0 Z" fill="var(--wave-1)" stroke="var(--wave-line)" stroke-width="1"/>
      <path d="M700 60 C650 150 640 230 580 300 C530 370 520 440 500 500 L800 500 L800 40 Z" fill="var(--wave-2)" stroke="var(--wave-line)" stroke-width="1"/>
      <path d="M800 160 C740 220 710 300 660 360 C620 410 610 460 600 500 L800 500 Z" fill="var(--wave-3)" stroke="var(--wave-line)" stroke-width="1"/>
      <path d="M800 320 C760 370 740 430 720 500 L800 500 Z" fill="var(--wave-4)"/>
    </svg>
    <div class="brand">
      <span class="brand__name">Marta &amp; das Lindenwäldchen</span>
      <span class="brand__claim">Urlaub an einem besonderen Ort</span>
    </div>
  </section>

  <section class="card card--back" aria-label="Visitenkarte Rückseite">
    <svg class="card__waves" viewBox="0 0 800 500" preserveAspectRatio="none" aria-hidden="true">
      <path d="M640 0 C600 110 620 180 560 260 C510 340 500 420 470 500 L800 500 L800 0 Z" fill="var(--wave-1)" stroke="var(--wave-line)" stroke-width="1"/>
      <path d="M760 50 C710 150 700 230 640 300 C600 360 580 440 560 500 L800 500 L800 40 Z" fill="var(--wave-2)" stroke="var(--wave-line)" stroke-width="1"/>
      <path d="M800 170 C750 240 730 310 690 370 C660 420 650 460 640 500 L800 500 Z" fill="var(--wave-3)" stroke="var(--wave-line)" stroke-width="1"/>
      <path d="M800 330 C770 380 750 440 735 500 L800 500 Z" fill="var(--wave-4)"/>
    </svg>
    <p class="tagline">Entspannen - Loslassen - Auftanken</p>
    <div class="brand">
      <span class="brand__name">Marta &amp; das Lindenwäldchen</span>
      <span class="brand__claim">Urlaub an einem besonderen Ort</span>
    </div>
    <address class="contact contact--online">
      post@marta-brecke.de<br>
      www.lindenwaeldchen.net
    </address>
    <address class="contact contact--address">
      Marta Brecke<br>
      Grauer Pfad 7<br>
      18471 Alt Feldow
    </address>
  </section>

</body>
</html>
```